Aviation Banner Ad Designs

SkyLedgerMetrics provides access to the most accurate aircraft operating cost information, to compare Piston, Turboprop and Jet aircraft.

The banners ads will be used for retargeting/remarketing - to bring visitors back to the site. The banners should remind and reinforce the key messages of what the site provides.

Target Market(s)

Private aircraft buyers including:
- Aircraft Brokers
- Charter Operators
- Corporate Flight Departments
- Aircraft Management companies
- Financial Institutions
- Aircraft Owners
- Prospective Buyers

Requirements
Must have
• A. Banner Objective
The visual and textual content of the banner should remind the viewer about the features of the site, and prompt them to return to the site.
1. Arresting visual
2. Headline
3. Single message
4. Compelling CTA
5. Logo - big enough to see
6. Standard DWR ad sizes/specs

B. Design Elements
Logo: As attached
Main Title: Calculate Jet Operating Costs
Subtitle: Compare Ownership Usage Scenarios
Call to Action Button: Compare Ownership Costs
Background: Several images supplied as options

C. Banner Sizes
Do examples as 300×250 , 728×90 , 160×600
Final sizes to also include 320×100 , 336x280 , 300x600

Finally delivery as .jpg files.

Font - use same font as on site

```html
<!DOCTYPE html>
<html lang="en">
<head>
<meta charset="utf-8">
<title>SkyLedgerMetrics Banner Set</title>
<link rel="stylesheet" href="https://fonts.googleapis.com/css2?family=Bebas+Neue&family=Roboto:wght@400;500&display=swap">
<style>
  :root {
    --navy: #0b1a5c;
    --navy-deep: #081449;
    --stripe: #1f6fc4;
    --red: #e0262c;
    --green-top: #52c94a;
    --green-bottom: #1c8e22;
    --white: #ffffff;
    --sky-warm: #e9b98a;
    --sky-grey: #9c9a9c;
    --sky-dark: #5d5660;
  }
  html, body { margin: 0; padding: 0; overflow: hidden; }
  body {
    width: 1200px; height: 536px; position: relative;
    background: var(--white);
    font-family: "Roboto", Arial, sans-serif;
  }
  .banner {
    position: absolute; overflow: hidden; background: var(--navy);
    box-shadow: 0 6px 22px rgba(0,0,0,0.22);
  }
  .photo {
    position: absolute;
    background: linear-gradient(160deg, var(--sky-grey) 0%, var(--sky-warm) 55%, var(--sky-dark) 100%);
  }
  .headline {
    font-family: "Bebas Neue", Impact, sans-serif;
    color: var(--red); margin: 0; text-align: center; line-height: 0.86;
  }
  .subtitle { color: var(--white); text-align: center; margin: 0; }
  .cta {
    position: absolute; display: flex; align-items: center; justify-content: center; gap: 8px;
    border: 2px solid var(--white); border-radius: 999px;
    background: linear-gradient(var(--green-top), var(--green-bottom));
    color: var(--white); font-family: "Bebas Neue", Impact, sans-serif;
    box-sizing: border-box; box-shadow: 0 2px 4px rgba(0,0,0,0.3);
  }
  .cta svg { flex: none; }
  .brand {
    position: absolute; display: flex; align-items: center; justify-content: center; gap: 8px;
    background: var(--white); color: var(--navy);
    font-family: "Roboto", Arial, sans-serif; font-weight: 500;
  }
  .brand-mark { flex: none; background: var(--red); }
  .decor { position: absolute; border-radius: 50%; background: var(--navy-deep); opacity: .6; }

  /* Medium rectangle 300x250 */
  .medium { left: 307px; top: 61px; width: 357px; height: 298px; }
  .medium .photo { inset: 0 0 auto 0; height: 165px; }
  .medium .band { position: absolute; left: 0; top: 0; width: 357px; height: 298px; }
  .medium .cta { left: 86px; top: 103px; width: 186px; height: 40px; font-size: 17px; }
  .medium .headline { position: absolute; left: 0; right: 0; top: 160px; font-size: 42px; }
  .medium .subtitle { position: absolute; left: 0; right: 0; top: 227px; font-size: 11.5px; }
  .medium .brand { left: 62px; top: 249px; width: 224px; height: 60px; border-radius: 112px 112px 0 0 / 40px 40px 0 0; font-size: 15px; padding-bottom: 10px; box-sizing: border-box; }
  .medium .brand-mark { width: 14px; height: 14px; }

  /* Leaderboard 728x90 */
  .leader { left: 79px; top: 374px; width: 867px; height: 107px; }
  .leader .band { position: absolute; inset: 0; }
  .leader .brand { left: 0; top: 0; width: 250px; height: 107px; background: transparent; font-size: 22px; z-index: 1; }
  .leader .brand-mark { width: 18px; height: 18px; }
  .leader .headline { position: absolute; left: 300px; width: 282px; top: 13px; font-size: 45px; }
  .leader .subtitle { position: absolute; left: 300px; width: 282px; top: 86px; font-size: 11.5px; }
  .leader .cta { left: 608px; top: 27px; width: 218px; height: 48px; font-size: 20px; }

  /* Skyscraper 160x600 */
  .sky { left: 967px; top: 50px; width: 116px; height: 432px; }
  .sky .photo { inset: auto 0 0 0; height: 112px; }
  .sky .band { position: absolute; inset: 0; }
  .sky .brand { left: 0; top: 0; width: 116px; height: 46px; border-radius: 0 0 18px 18px; font-size: 11px; gap: 5px; }
  .sky .brand-mark { width: 9px; height: 9px; }
  .sky .headline { position: absolute; left: 0; right: 0; top: 79px; }
  .sky .headline span { display: block; }
  .sky .subtitle { position: absolute; left: 0; right: 0; top: 213px; font-size: 8px; line-height: 10px; }
  .sky .cta { left: 10px; top: 269px; width: 98px; height: 23px; font-size: 8px; gap: 4px; }
</style>
</head>
<body>

<section class="banner medium" aria-label="300 by 250 banner">
  <div class="photo" role="img" aria-label="Business jet climbing through a warm sunset sky"></div>
  <svg class="band" viewBox="0 0 357 298" aria-hidden="true">
    <polygon points="0,132 357,91 357,298 0,298" fill="var(--stripe)"/>
    <polygon points="0,139 357,98 357,298 0,298" fill="var(--navy)"/>
  </svg>
  <div class="decor" style="left:-20px;top:160px;width:80px;height:95px"></div>
  <div class="decor" style="left:318px;top:130px;width:70px;height:90px"></div>
  <a class="cta">COMPARE OWNERSHIP COSTS
    <svg width="8" height="13" viewBox="0 0 8 13"><path d="M1 1l5.5 5.5L1 12" stroke="#fff" stroke-width="2" fill="none"/></svg></a>
  <h1 class="headline">CALCULATE JET<br>OPERATING COSTS</h1>
  <p class="subtitle">COMPARE OWNERSHIP USAGE SCENARIOS</p>
  <div class="brand"><span class="brand-mark"></span>SkyLedgerMetrics</div>
</section>

<section class="banner leader" aria-label="728 by 90 banner">
  <svg class="band" viewBox="0 0 867 107" preserveAspectRatio="none" aria-hidden="true">
    <polygon points="0,0 274,0 221,107 0,107" fill="var(--stripe)"/>
    <polygon points="0,0 269,0 216,107 0,107" fill="var(--white)"/>
  </svg>
  <div class="decor" style="left:250px;top:60px;width:90px;height:90px"></div>
  <div class="decor" style="left:730px;top:-30px;width:90px;height:60px"></div>
  <div class="brand"><span class="brand-mark"></span>SkyLedgerMetrics</div>
  <h2 class="headline">CALCULATE JET<br>OPERATING COSTS</h2>
  <p class="subtitle">COMPARE OWNERSHIP USAGE SCENARIOS</p>
  <a class="cta">COMPARE OWNERSHIP COSTS
    <svg width="9" height="15" viewBox="0 0 9 15"><path d="M1 1l6.5 6.5L1 14" stroke="#fff" stroke-width="2" fill="none"/></svg></a>
</section>

<section class="banner sky" aria-label="160 by 600 banner">
  <div class="photo" role="img" aria-label="Business jet in flight against sunset clouds"></div>
  <svg class="band" viewBox="0 0 116 432" aria-hidden="true">
    <polygon points="0,0 116,0 116,321 0,336" fill="var(--stripe)"/>
    <polygon points="0,0 116,0 116,316 0,331" fill="var(--navy)"/>
  </svg>
  <div class="decor" style="left:90px;top:70px;width:50px;height:80px"></div>
  <div class="brand"><span class="brand-mark"></span>SkyLedgerMetrics</div>
  <h2 class="headline">
    <span style="font-size:27px">CALCULATE</span>
    <span style="font-size:30px">JET</span>
    <span style="font-size:27px">OPERATING</span>
    <span style="font-size:40px">COSTS</span>
  </h2>
  <p class="subtitle">COMPARE<br>OWNERSHIP<br>USAGE<br>SCENARIOS</p>
  <a class="cta">COMPARE OWNERSHIP COSTS
    <svg width="5" height="8" viewBox="0 0 5 8"><path d="M1 1l3 3-3 3" stroke="#fff" stroke-width="1.2" fill="none"/></svg></a>
</section>

</body>
</html>
```